Business Card Design Project - IT Company

Kestrafield Information Technology Solutions
We are an Information Technology Company. We provide computer services to commercial companies. We would like a new card full color front and back with bleeding edge.
We have a logo that you can use or if you want to come up with a new logo that is fine too.
Our colors are mostly Maroon and black but be creative.
Sample Information
Brent R Okafor
4812 W Saguaro Ridge Drive
Suite 600
Phoenix, AZ 85016
O: 602.914.2037
C: 602.468.1290
24/7: 888.914.2037
bokafor@kestrafield.example
www.kestrafield.example
Target Market(s)
Business of all sizes
Industry/Entity Type
Computer
Requirements
Must have
- Bleeding edge
full color on both sides

```html
<!DOCTYPE html>
<html lang="en">
<head>
<meta charset="utf-8">
<title>Kestrafield Information Technology Solutions – Business Card</title>
<link rel="stylesheet" href="https://fonts.googleapis.com/css2?family=Open+Sans:wght@700&family=Tinos&display=swap">
<style>
  :root {
    --backdrop: #000000;
    --maroon-light: #d5133a;
    --maroon-mid: #c4112e;
    --maroon-deep: #9e111c;
    --card-edge: #ffffff;
    --logo-grey: #505053;
    --tagline-grey: #5c5c5e;
  }
  html, body {
    margin: 0;
    padding: 0;
    overflow: hidden;
    background: var(--backdrop);
  }
  .canvas {
    position: relative;
    width: 1200px;
    height: 695px;
    overflow: hidden;
    background: var(--backdrop);
  }
  .card-shape {
    position: absolute;
    inset: 0;
    width: 1200px;
    height: 695px;
  }
  .brand {
    position: absolute;
    left: 0;
    right: 0;
    top: 248px;
    text-align: center;
  }
  .brand-name {
    margin: 0;
    font-family: "Open Sans", Arial, sans-serif;
    font-weight: 700;
    font-size: 84px;
    line-height: 1;
    letter-spacing: 12px;
    text-transform: uppercase;
    color: var(--logo-grey);
  }
  .brand-tagline {
    margin: 44px 0 0;
    font-family: "Tinos", "Times New Roman", serif;
    font-size: 37px;
    line-height: 1;
    color: var(--tagline-grey);
  }
</style>
</head>
<body>
  <main class="canvas">
    <svg class="card-shape" viewBox="0 0 1200 695" aria-hidden="true">
      <defs>
        <linearGradient id="card-fill" x1="0" y1="0" x2="0" y2="1">
          <stop offset="0" stop-color="var(--maroon-light)"/>
          <stop offset="0.5" stop-color="var(--maroon-mid)"/>
          <stop offset="1" stop-color="var(--maroon-deep)"/>
        </linearGradient>
        <radialGradient id="card-shade" cx="0.5" cy="0.5" r="0.65">
          <stop offset="0.6" stop-color="#000" stop-opacity="0"/>
          <stop offset="1" stop-color="#000" stop-opacity="0.28"/>
        </radialGradient>
      </defs>
      <path class="card-body"
            d="M62 0 C 95 140, 112 250, 112 347 C 112 445, 95 555, 62 695
               L 1123 695 C 1090 555, 1070 445, 1070 347 C 1070 250, 1090 140, 1123 0 Z"
            fill="url(#card-fill)"/>
      <path class="card-vignette"
            d="M62 0 C 95 140, 112 250, 112 347 C 112 445, 95 555, 62 695
               L 1123 695 C 1090 555, 1070 445, 1070 347 C 1070 250, 1090 140, 1123 0 Z"
            fill="url(#card-shade)"/>
      <path class="card-edge-left" d="M62 0 C 95 140, 112 250, 112 347 C 112 445, 95 555, 62 695"
            fill="none" stroke="var(--card-edge)" stroke-width="2.5"/>
      <path class="card-edge-right" d="M1123 0 C 1090 140, 1070 250, 1070 347 C 1070 445, 1090 555, 1123 695"
            fill="none" stroke="var(--card-edge)" stroke-width="2.5"/>
    </svg>

    <section class="brand">
      <h1 class="brand-name">Kestrafield</h1>
      <p class="brand-tagline">Information Technology Solutions</p>
    </section>
  </main>
</body>
</html>
```